QRN Law Letterhead

Want law firm letterhead - both in terms of a pdf file that I can use electronically as letterhead by adding it as a background - and in terms of a file that I can send to a company to create actual letterhead.
Industry/Entity Type
Law Firm
Font styles to use
Sans Serif
Requirements
Must have
- Should have the following information (you can decide where to place):
- My name - Emil Vostrakian
- My email - emil@qrnlegalgroup.example
- My address - 2861 Corvella Parkway 318-742
- San Jose, California 95342
- Website - www.qrnlegalgroup.example
- Phone - 408-297-1586
- Fax - 408-853-2941
- The logo I attached
Nice to have
- I think I would prefer to have a black and white color scheme.
- I don't necessarily need a title after my name, but I have seen a few design submissions that include a generic title. The title I would use is "IP Litigator & Trademark Attorney"

```html
<!DOCTYPE html>
<html lang="en">
<head>
<meta charset="utf-8">
<title>QRN Law Letterhead</title>
<link rel="stylesheet" href="https://fonts.googleapis.com/css2?family=Montserrat:wght@600&family=Roboto:wght@400;500;700&display=swap">
<style>
  :root {
    --backdrop: #c9c5c9;
    --paper: #ffffff;
    --ink: #111111;
    --band: #121212;
    --band-text: #e8e8e8;
    --faint: #d6d6d6;
  }
  html, body {
    margin: 0;
    width: 1200px;
    height: 1200px;
    overflow: hidden;
    background: var(--backdrop);
  }
  .letterhead {
    position: absolute;
    left: 300px;
    top: 210px;
    width: 602px;
    height: 780px;
    background: var(--paper);
    font-family: "Roboto", Arial, sans-serif;
    color: var(--ink);
  }
  .brand {
    position: absolute;
    top: 30px;
    left: 0;
    right: 0;
    display: flex;
    justify-content: center;
    align-items: center;
    gap: 10px;
    font-family: "Montserrat", Arial, sans-serif;
    font-weight: 600;
    font-size: 38px;
    letter-spacing: 1px;
    color: var(--ink);
  }
  .brand-dot {
    width: 26px;
    height: 26px;
    border-radius: 50%;
    background: var(--ink);
  }
  .backdrop-name {
    position: absolute;
    top: 330px;
    left: 0;
    right: 0;
    text-align: center;
    font-family: "Montserrat", Arial, sans-serif;
    font-weight: 600;
    font-size: 96px;
    color: var(--faint);
    letter-spacing: 2px;
  }
  .signatory {
    position: absolute;
    left: 61px;
    top: 664px;
    font-weight: 700;
    font-size: 11px;
    letter-spacing: 0.2px;
    text-transform: uppercase;
  }
  .contact-band {
    position: absolute;
    left: 0;
    bottom: 0;
    width: 100%;
    height: 42px;
    background: var(--band);
    color: var(--band-text);
    font-size: 8.5px;
    line-height: 1.35;
  }
  .contact-item {
    position: absolute;
    top: 0;
    height: 42px;
    display: flex;
    align-items: center;
    gap: 8px;
  }
  .contact-item svg { width: 11px; height: 11px; flex: none; }
  .contact-phones { left: 29px; flex-direction: column; align-items: flex-start; justify-content: center; gap: 2px; }
  .contact-phones .line { display: flex; align-items: center; gap: 8px; }
  .contact-phones svg { width: 9px; height: 9px; }
  .contact-email { left: 128px; }
  .contact-web { left: 267px; }
  .contact-address { left: 396px; }
</style>
</head>
<body>
  <main class="letterhead">
    <header class="brand"><span class="brand-dot"></span>QRN Law</header>

    <div class="backdrop-name" aria-hidden="true">QRN Law</div>

    <p class="signatory" style="margin:0">Emil Vostrakian</p>

    <footer class="contact-band">
      <div class="contact-item contact-phones">
        <div class="line">
          <svg viewBox="0 0 12 12" aria-label="Phone"><circle cx="6" cy="6" r="6" fill="#e8e8e8"/><path d="M4 3.2l1.1 1.5-.6.8c.4.9 1.1 1.6 2 2l.8-.6 1.5 1.1-.6 1c-2.6-.2-4.7-2.3-4.9-4.9z" fill="#121212"/></svg>
          <span>408-297-1586</span>
        </div>
        <div class="line">
          <svg viewBox="0 0 12 12" aria-label="Fax"><rect x="3" y="1" width="6" height="3.5" fill="#e8e8e8"/><rect x="1" y="4.5" width="10" height="4.5" rx="1" fill="#e8e8e8"/><rect x="3" y="7.5" width="6" height="3.5" fill="#e8e8e8" stroke="#121212" stroke-width="0.8"/></svg>
          <span>408-853-2941</span>
        </div>
      </div>

      <div class="contact-item contact-email">
        <svg viewBox="0 0 12 12" aria-label="Email"><circle cx="6" cy="6" r="6" fill="#e8e8e8"/><rect x="3" y="4" width="6" height="4.2" fill="#121212"/><path d="M3 4l3 2.3L9 4" stroke="#e8e8e8" stroke-width="0.7" fill="none"/></svg>
        <span>emil@qrnlegalgroup.example</span>
      </div>

      <div class="contact-item contact-web">
        <svg viewBox="0 0 12 12" aria-label="Website"><circle cx="6" cy="6" r="6" fill="#e8e8e8"/><circle cx="6" cy="6" r="3.2" fill="none" stroke="#121212" stroke-width="0.8"/><path d="M2.8 6h6.4M6 2.8c-1.4 1.8-1.4 4.6 0 6.4M6 2.8c1.4 1.8 1.4 4.6 0 6.4" stroke="#121212" stroke-width="0.6" fill="none"/></svg>
        <span>www.qrnlegalgroup.example</span>
      </div>

      <div class="contact-item contact-address">
        <svg viewBox="0 0 12 12" aria-label="Address"><circle cx="6" cy="6" r="6" fill="#e8e8e8"/><path d="M6 2.6a2.3 2.3 0 0 1 2.3 2.3C8.3 6.6 6 9.4 6 9.4S3.7 6.6 3.7 4.9A2.3 2.3 0 0 1 6 2.6z" fill="#121212"/><circle cx="6" cy="4.9" r="0.9" fill="#e8e8e8"/></svg>
        <span>2861 Corvella Parkway 318-742<br>San Jose, California 95342</span>
      </div>
    </footer>
  </main>
</body>
</html>
```